Dr Tasneer's Letterhead

I need a professional neat letterhead incorporating my professional information, university titles and qualifications. I have attached my 3 recent ones which contain all the necessary information that needs to be included. I am happy for the information to be a side bar left or right, or as a header/footer combination.

Hello all

I have now made a 2nd and 3rd prize so please submit

Reason: Now there is a 2nd and 3rd place so I can take 3 designs

Industry/Entity Type

University

```html
<!DOCTYPE html>
<html lang="en">
<head>
<meta charset="utf-8">
<title>Dr Tasneer Letterhead</title>
<link rel="stylesheet" href="https://fonts.googleapis.com/css2?family=Exo+2:wght@300;400;500;600&display=swap">
<style>
  :root {
    --backdrop: #ebebeb;
    --paper: #f8f8f8;
    --mint: #6cc4a1;
    --mint-deep: #4fae8a;
    --ink: #6f6f6f;
    --ink-dark: #2f4a40;
    --placeholder: #d6d6d6;
  }
  * { box-sizing: border-box; margin: 0; padding: 0; }
  html, body { width: 1200px; height: 1000px; overflow: hidden; }
  body {
    background: var(--backdrop);
    font-family: "Exo 2", sans-serif;
    color: var(--ink);
  }
  .letterhead {
    position: absolute;
    left: 270px; top: 33px;
    width: 660px; height: 934px;
    background: var(--paper);
    box-shadow: 0 2px 10px rgba(0,0,0,.08);
  }
  .masthead {
    position: absolute; left: 0; top: 0;
    width: 478px; height: 108px;
    background: var(--mint);
    padding: 14px 0 0 30px;
  }
  .masthead__name {
    font-size: 31px; font-weight: 500; color: #fff; letter-spacing: .3px;
    line-height: 1;
  }
  .masthead__credentials {
    margin-top: 10px;
    font-size: 7.5px; line-height: 1.35; color: var(--ink-dark); font-weight: 400;
    list-style: none;
  }
  .letter {
    position: absolute; left: 60px; right: 60px; top: 205px;
    font-size: 10px; line-height: 1.7; font-weight: 300;
  }
  .letter__salutation { margin-bottom: 6px; }
  .letter__subject {
    text-align: right; margin: -10px 0 14px;
    color: var(--mint-deep); font-size: 15px; font-weight: 600;
  }
  .letter p { margin-bottom: 16px; text-align: left; }
  .letter__signoff { margin-top: 4px; }
  .signature {
    position: absolute; left: 345px; top: 545px;
    width: 200px; height: 70px; border-radius: 6px;
    background: linear-gradient(90deg, #ececec, #e3e3e3);
  }
  .footer-rule {
    position: absolute; left: 0; right: 0; top: 798px; height: 8px;
    background: var(--mint);
  }
  .footer-band {
    position: absolute; left: 0; right: 0; bottom: 0; height: 14px;
    background: var(--mint);
  }
  .practices {
    position: absolute; left: 20px; top: 816px; width: 210px;
    text-align: right; font-size: 8px; line-height: 1.7; color: var(--ink);
    list-style: none;
  }
  .contacts {
    position: absolute; left: 246px; top: 814px;
    padding-left: 14px; border-left: 1.5px solid var(--mint);
    font-size: 8px; line-height: 1.9; list-style: none;
  }
  .contacts li { display: flex; align-items: center; gap: 6px; }
  .contacts svg { width: 8px; height: 8px; fill: var(--mint-deep); }
  .affiliations {
    position: absolute; right: 40px; top: 860px;
    display: flex; align-items: center; gap: 5px;
  }
  .affiliations__badge {
    width: 16px; height: 18px; background: var(--placeholder);
  }
  .affiliations__college {
    width: 46px; height: 18px; background: var(--placeholder); margin-left: 3px;
  }
  .provider-numbers {
    position: absolute; right: 40px; top: 885px;
    font-size: 6.5px; color: var(--ink-dark);
  }
</style>
</head>
<body>
<main class="letterhead">
  <header class="masthead">
    <h1 class="masthead__name">Dr. Arman Tasneer</h1>
    <ul class="masthead__credentials">
      <li>BSc Med, MBBS (Hons I), FRCS (Oto-HNS)</li>
      <li>Consultant ENT Head and Neck Surgeon</li>
      <li>Senior Staff Specialist, Northbridge Health District</li>
      <li>Visiting Surgeon, Harbourview Cancer Centre</li>
      <li>Senior Lecturer, Eastvale University School of Medicine</li>
    </ul>
  </header>

  <section class="letter">
    <p class="letter__salutation">Dear Client,</p>
    <h2 class="letter__subject">Lorem ipsum dolor sit ametconsectetur.</h2>
    <p>Lorem ipsum dolor sit amet, consectetur adipiscing elit. Nulla sodales nisi vitae Lorem ipsum dolor sit amet, consectetur adipiscing elit. Suspendisse feugiat eros nisi, a facilisis risus eleifend sed. Aliquam mauris enim, fermentum eu lacinia sit amet, laoreet eu leo. Nullam eleifend nulla in libero tristique ac vulputate odio tincidunt. Etiam non condimentum tortor. Integer suscipit neque nec odio porttitor cursus. Phasellus a sapien blandit, suscipit justo id, condimentum ante. Morbi tristique justo risus, id mattis dui molestie ut. Nullam volutpat ut quam commodo faucibus. Pellentesque urna est, interdum in elit quis, pharetra elementum orci. Nam pharetra velit molestie justo placerat scelerisque.</p>
    <p>Ut vitae interdum diam, in euismod ante. Pellentesque volutpat, risus sit amet sodales hendrerit, mi turpis vulputate dolor, eget cursus nulla eros nec tellus. Nulla tincidunt molestie libero vel pretium. Donec condimentum nulla sit amet risus semper imperdiet. Duis congue eros nec diam blandit, et pellentesque sapien auctor. Curabitur iaculis enim lectus, in imperdiet mauris mattis eget. Etiam ac ornare metus. Mauris risus leo, egestas at dolor a, ultrices adipiscing erat. Nunc faucibus scelerisque mollis. Pellentesque aliquet mauris tellus, id dignissim risus viverra et. Mauris venenatis lobortis eros. Nam id diam in ligula malesuada feugiat. Cras turpis felis, aliquet id mauris elementum, feugiat ultricies nisl.</p>
    <p class="letter__signoff">Best regards,</p>
  </section>

  <div class="signature" role="img" aria-label="Handwritten signature of Dr. Arman Tasneer"></div>

  <div class="footer-rule"></div>

  <ul class="practices">
    <li>Suite 12/48 Linden Parade, Eastvale 2190</li>
    <li>7 Marlow Avenue, Northbridge 2172</li>
    <li>31 Orchard Lane, Riverton 2744</li>
  </ul>

  <ul class="contacts">
    <li><svg viewBox="0 0 10 10"><path d="M2 0.5l2 2-1 1.3c.6 1.3 1.6 2.3 2.9 2.9L7.2 5.7l2 2-1.3 1.8C4.3 9.3.7 5.7.5 1.8z"/></svg>84210567 / 84219032</li>
    <li><svg viewBox="0 0 10 10"><path d="M2 0h5v3H2zM0 3.5h10V8H8v2H2V8H0zM3 6.5v2.5h4V6.5z"/></svg>95550142</li>
    <li><svg viewBox="0 0 10 10"><circle cx="5" cy="5" r="4.5"/></svg>www.drtasneer.com</li>
  </ul>

  <div class="affiliations" role="img" aria-label="Professional affiliation badges">
    <span class="affiliations__badge"></span>
    <span class="affiliations__badge"></span>
    <span class="affiliations__badge"></span>
    <span class="affiliations__college"></span>
  </div>
  <p class="provider-numbers">Provider 4021836X, 2053147A, 2460592K</p>

  <div class="footer-band"></div>
</main>
</body>
</html>
```